Business Cards for a Junk Removal Company

Hello,
We are looking to have business cards designed that are simple, bold, easy to read, and right to the point. Please see the attachments for our logo files. We want the card to be yellow on both sides ( Color code Yellow: #FFE01B). The logo text font is (Rockstar Extra Bold) and this is also in the files attached. Please make the text black for the logo. On the back side of the card, you can use white and black for text. Thank you in advance for your hard work!

Front of card-
Harbor Haul Removal (logo)
Back of card-
Harbor Haul Removal
Donate - Recycle - Dispose
518-276-9053
www.harborhaulremoval.example
info@harborhaulremoval.example

Industry/Entity Type

Junk removal

Contact Information for Business Card

FRONT OF CARD- Harbor Haul Removal (logo) BACK OF CARD- Harbor Haul Removal Donate - Recycle - Dispose 518-276-9053 www.harborhaulremoval.example info@harborhaulremoval.example

Font styles to use
Other font styles liked:
• Rockstar Extra Bold

Colors
FFF300
FFF600
FEFA6F
FFFEC7
FFFEE8

Requirements
Must have
• Must have color code Yellow: #FFE01B for the background of front and back of the card

```html
<!DOCTYPE html>
<html lang="en">
<head>
<meta charset="utf-8">
<title>Harbor Haul Removal — Business Cards</title>
<link href="https://fonts.googleapis.com/css2?family=Saira+Condensed:wght@600;700;800;900&display=swap" rel="stylesheet">
<style>
  :root {
    --card-yellow: #FFE01B;
    --ink-black: #111111;
    --backdrop: #6a5744;
    --card-shadow: rgba(0, 0, 0, 0.45);
  }
  * { margin: 0; padding: 0; box-sizing: border-box; }
  html, body {
    width: 900px;
    height: 1200px;
    overflow: hidden;
    background: var(--backdrop);
  }
  body {
    position: relative;
    font-family: "Saira Condensed", "Arial Narrow", sans-serif;
    color: var(--ink-black);
  }
  .card {
    position: absolute;
    background: var(--card-yellow);
    border-radius: 40px;
    overflow: hidden;
    box-shadow: 0 6px 14px var(--card-shadow);
  }

  /* Contact side */
  .card--contact {
    left: 73px; top: 113px;
    width: 762px; height: 445px;
  }
  .brand-name {
    font-weight: 900;
    text-transform: uppercase;
    line-height: 0.9;
    color: var(--ink-black);
  }
  .card--contact .brand-name {
    position: absolute;
    left: 64px; top: 150px;
    width: 260px;
    font-size: 50px;
    letter-spacing: 0.5px;
  }
  .divider {
    position: absolute;
    left: 346px; top: 155px;
    width: 3px; height: 95px;
    background: var(--ink-black);
  }
  .contact-list {
    position: absolute;
    left: 371px; top: 150px;
    list-style: none;
  }
  .contact-list li { white-space: nowrap; }
  .contact-phone {
    display: flex;
    align-items: center;
    gap: 12px;
    font-size: 36px;
    font-weight: 800;
    line-height: 40px;
    letter-spacing: 0.5px;
  }
  .contact-phone svg { width: 24px; height: 24px; flex: none; }
  .contact-web, .contact-mail {
    font-size: 23px;
    font-weight: 700;
    line-height: 34px;
    letter-spacing: 0.6px;
  }
  .contact-web { margin-top: 4px; }
  .tagline-band {
    position: absolute;
    left: 0; bottom: 0;
    width: 100%; height: 83px;
    background: var(--ink-black);
    color: var(--card-yellow);
    display: flex;
    align-items: center;
    justify-content: center;
    font-size: 46px;
    font-weight: 800;
    letter-spacing: 1.5px;
    text-transform: uppercase;
  }

  /* Logo side */
  .card--logo {
    left: 67px; top: 640px;
    width: 763px; height: 445px;
  }
  .card--logo .brand-name {
    position: absolute;
    left: 0; top: 148px;
    width: 100%;
    text-align: center;
    font-size: 78px;
    letter-spacing: 1px;
  }
  .logo-url {
    position: absolute;
    left: 0; top: 393px;
    width: 100%;
    text-align: center;
    font-size: 21px;
    font-weight: 800;
    letter-spacing: 1.4px;
    text-transform: uppercase;
  }
</style>
</head>
<body>

  <section class="card card--contact" aria-label="Business card, contact side">
    <h1 class="brand-name">Harbor Haul Removal</h1>
    <div class="divider"></div>
    <ul class="contact-list">
      <li class="contact-phone">
        <svg viewBox="0 0 24 24" aria-hidden="true">
          <rect x="1.5" y="1.5" width="21" height="21" rx="2" fill="none" stroke="#111" stroke-width="3"/>
          <path d="M8 6.5c-.6 0-1.4.8-1.4 1.7 0 3.6 5.6 9.2 9.2 9.2.9 0 1.7-.8 1.7-1.4l-.1-.6-2.4-1.2-1.3 1.2c-1.7-.8-3.4-2.5-4.2-4.2l1.2-1.3-1.2-2.4z" fill="#111"/>
        </svg>
        518-276-9053
      </li>
      <li class="contact-web">www.harborhaulremoval.example</li>
      <li class="contact-mail">info@harborhaulremoval.example</li>
    </ul>
    <div class="tagline-band">Donate - Recycle - Dispose</div>
  </section>

  <section class="card card--logo" aria-label="Business card, logo side">
    <h2 class="brand-name">Harbor Haul<br>Removal</h2>
    <p class="logo-url">www.harborhaulremoval.example</p>
  </section>

</body>
</html>
```